Truck Outfitters and Trailer Hitch Retailer Website

We are working with a hitch installer in California called Brisk Coupler. They sell and install trailer hitches, bedliners for trucks, and pickup truck accessories.
Some sites to use for content/competitors:
https://www.marvelko.com/pick-up-outfitters
https://brandels-rigs.com
https://www.thetowpalace.com
https://towpalaceinccom.sitebuildhost.com
Some sites to use for inspiration:
https://www.ironwallcouplers.com
https://quietlinkcouplers.com
https://novatow.com/
https://www.veranbedcoat.com
https://www.rugged-trailworks.com
Thank you for taking the time to consider designing a website for us. We are web developers based in Stockton, CA, USA. Most of our projects go through the same process. Understanding this process may help you win a project with us. We custom-code all of our websites in-house. We don’t have any requirements as to what tools you use for your design, but we prefer Sketchra files. For any design that we label as four-stars, we send it to the client for review. The client picks the final design they want us to use. Once we complete this process, we will continue to show additional clients all the four-star sites and purchase them later. Your designs will have multiple chances to sell. For better chances of success, we ask that you follow these guidelines.
IMAGES:
If you use any images or icons in the design, we ask that you have a link to the asset so we can purchase the image/icon. Most of the designs we submit do not have the customer’s images on them unless they have some great images. Be creative; show us the feeling you are trying to portray with your image choices. Use any royalty-free site you choose. We subscribe to Pixtrove and mainly use their images, but we can purchase images outside of Pixtrove.
PLEASE NOTE: we will not submit designs to clients with watermarks on the images.
FONTS:
We ask that you identify the fonts used in the design. This can be done in a message if you want. We typically use Google Fonts and Pixtrove Fonts.
CONTENT:
We're always open to different content and ideas. We often submit designs with stock images so the client can see our vision. We typically take pictures after the website launch to use their images with our vision. Lorem Ipsum is fine for paragraphs, but we ask that you write the headers in correct English. We want to be able to show the vision and identify the sections of the website.
INSPIRATION:
We typically add a couple of links in the brief of websites we like to help you get started in your design.
REVISIONS:
We do not often ask for revisions of the designs unless we see something in the design that may not appeal to the client. If there are slight changes that we want to make, we do that in the development process.
FEEDBACK:
We rarely give feedback on designs during the design process. We are working on many website projects and do not have the time to provide feedback. We usually respond if your request is well thought out and asks specific questions, but a note asking “feedback, please” usually goes unanswered

```html
<!DOCTYPE html>
<html lang="en">
<head>
<meta charset="utf-8">
<title>Brisk Coupler — Trailer Hitches & Truck Accessories</title>
<link href="https://fonts.googleapis.com/css2?family=Michroma&family=Poppins:wght@400;500;600;700&display=swap" rel="stylesheet">
<style>
:root{
  --red:#e8270f;
  --red-deep:#c41d08;
  --ink:#1c1c1c;
  --charcoal:#2b2b2b;
  --night:#161616;
  --white:#ffffff;
  --text:#444444;
  --muted:#8a8a8a;
  --line:#cfcfcf;
  --gold:#f2b01e;
  --display:"Michroma", sans-serif;
  --body:"Poppins", sans-serif;
}
*{box-sizing:border-box;margin:0;padding:0}
html,body{width:1200px;height:4766px;overflow:hidden}
body{font-family:var(--body);color:var(--text);background:var(--white);position:relative}
.abs{position:absolute}
section,header,footer,.band{position:absolute;left:0;width:1200px}
.display{font-family:var(--display);text-transform:uppercase;color:var(--ink);font-weight:400;line-height:1.25}
.btn{position:absolute;display:flex;align-items:center;justify-content:center;font-size:12.5px;font-family:var(--body);white-space:nowrap}
.btn-red{background:var(--red);color:var(--white);box-shadow:inset 0 0 0 2px var(--red),inset 0 0 0 3px rgba(255,255,255,.85)}
.btn-ghost{border:2px solid var(--white);color:var(--white)}
.eyebrow{position:absolute;font-size:11.5px;font-weight:600;text-transform:uppercase;letter-spacing:.3px}
.eyebrow::before{content:"";position:absolute;left:-98px;top:50%;width:85px;height:1px;background:var(--red)}

/* top bar */
.topbar{top:0;height:28px;background:#000;color:var(--white);font-size:9.5px}
.topbar .hours{left:92px;top:8px;display:flex;gap:14px}
.topbar .hours span+span{border-left:1px solid #666;padding-left:14px}
.topbar .mail{left:880px;top:8px;display:flex;align-items:center;gap:6px}
.social-dots{display:flex;gap:6px}
.social-dots i{display:block;width:14px;height:14px;border-radius:50%;background:var(--white)}
.topbar .social-dots{position:absolute;left:1047px;top:7px}

/* header */
.site-header{top:28px;height:87px;background:var(--white)}
.brand{position:absolute;display:flex;align-items:center;gap:10px;font-family:var(--display);text-transform:uppercase;font-size:18px;color:var(--charcoal)}
.brand i{display:block;width:38px;height:38px;background:var(--charcoal)}
.site-header .brand{left:94px;top:24px}
.nav{position:absolute;left:452px;top:38px;display:flex;gap:30px;font-size:11.5px;color:var(--ink)}
.callout{position:absolute;left:962px;top:0;width:238px;height:87px;background:var(--red);clip-path:polygon(12px 0,100% 0,100% 100%,0 100%)}
.callout small{position:absolute;left:76px;top:18px;font-size:9.5px;color:#ffe0da}
.callout strong{position:absolute;left:38px;top:36px;font-size:22px;font-weight:700;color:var(--white);letter-spacing:.3px}
.phone-disc{position:absolute;left:940px;top:27px;width:34px;height:34px;border-radius:50%;background:#111;display:flex;align-items:center;justify-content:center;border:2px solid var(--white)}

/* hero */
.hero{top:115px;height:555px;overflow:hidden;background:#0c0c0c}
.hero-photo{position:absolute;inset:0;background:radial-gradient(ellipse 420px 330px at 870px 240px,#8c8e92 0%,#4a4c50 35%,#1b1c1f 70%,#0b0b0c 100%)}
.hero-shade{position:absolute;inset:0;background:linear-gradient(90deg,rgba(0,0,0,.85) 0%,rgba(0,0,0,.6) 45%,rgba(0,0,0,0) 70%)}
.stripe{position:absolute;background:var(--red);transform:skewX(-40deg)}
.hero h1{position:absolute;left:92px;top:128px;font-size:34px;color:var(--white);line-height:55px;font-weight:400;white-space:nowrap}
.hero h1 span{display:block}
.hero h1 .indent{padding-left:143px;position:relative}
.hero h1 .indent::before{content:"";position:absolute;left:0;top:50%;width:133px;height:2px;background:var(--red)}
.hero p{position:absolute;left:92px;top:308px;width:420px;font-size:12.5px;line-height:1.75;color:#e9e9e9}

/* features band */
.features{top:670px;height:66px;background:var(--red);overflow:hidden}
.features .shard{position:absolute;top:0;height:66px;width:80px;background:var(--red-deep);transform:skewX(-35deg)}
.feature{position:absolute;top:18px;display:flex;align-items:center;gap:10px;color:var(--white);font-size:12px}
.feature i{display:flex;width:30px;height:30px;border:1.5px solid var(--white);border-radius:50%;align-items:center;justify-content:center}
.feature i::after{content:"";width:10px;height:10px;border:1.5px solid var(--white);border-radius:50%}

/* about */
.about{top:736px;height:623px;background:var(--white)}
.about .frame{position:absolute;left:0;top:155px;width:538px;height:360px;border:1.5px solid var(--line);border-left:0}
.about .photo{position:absolute;left:0;top:166px;width:560px;height:352px;background:linear-gradient(135deg,#a9aba7 0%,#6f716d 45%,#3d3f3c 100%)}
.about .photo-corner{position:absolute;left:548px;top:415px;width:12px;height:103px;background:#2a2a2a}
.about h2{position:absolute;left:620px;top:80px;font-size:23px;width:560px;line-height:1.55}
.about h3{position:absolute;left:620px;top:193px;font-size:10.5px;font-weight:600;color:var(--ink)}
.about .lead{position:absolute;left:620px;top:214px;width:480px;font-size:11.8px;line-height:1.62;color:#555}
.about .vertical{position:absolute;left:613px;top:354px;width:18px;height:80px;display:flex;align-items:center;justify-content:center}
.about .vertical span{transform:rotate(-90deg);white-space:nowrap;font-size:9.5px;font-weight:600;color:var(--ink)}
.about .vertical::after{content:"";position:absolute;left:22px;top:0;height:80px;width:1px;background:var(--line)}
.about .side{position:absolute;left:657px;top:360px;width:445px;font-size:11.8px;line-height:1.62;color:#555}

/* services */
.services{top:1359px;height:250px;background:var(--charcoal)}
.services .eyebrow{left:98px;top:58px;color:var(--white)}
.services h2{position:absolute;left:98px;top:88px;font-size:24px;color:var(--white)}
.services p{position:absolute;left:98px;top:137px;width:520px;font-size:12px;line-height:1.7;color:#dcdcdc}
.cards{top:1609px;height:414px;background:var(--white);display:flex;gap:2px}
.card{position:relative;flex:1;height:414px;overflow:hidden}
.card .media{position:absolute;inset:0}
.card .label{position:absolute;left:0;bottom:0;width:100%;height:50px;background:rgba(20,20,20,.88);color:var(--white);font-family:var(--display);text-transform:uppercase;font-size:11.5px;display:flex;align-items:center;justify-content:center}
.card-feature{background:var(--red);color:var(--white);text-align:center}
.card-feature h3{font-family:var(--display);text-transform:uppercase;font-weight:400;font-size:16px;line-height:26px;margin-top:68px;color:var(--white)}
.card-feature p{width:206px;margin:10px auto 0;font-size:11px;line-height:1.6}
.card-feature .btn{left:86px;top:306px;width:128px;height:40px;background:var(--charcoal);color:var(--white);border:1.5px solid #fff}

/* why */
.why{top:2023px;height:769px;background:var(--white)}
.why .watermark{position:absolute;left:30px;top:85px;width:200px;height:600px}
.why .watermark span{position:absolute;font-family:var(--display);text-transform:uppercase;font-size:72px;color:#efefef;white-space:nowrap;transform-origin:0 0;transform:rotate(-90deg)}
.why h2{position:absolute;left:0;width:1200px;text-align:center;top:100px;font-size:25px}
.why .emblem{position:absolute;left:430px;top:185px;width:340px;height:400px;border-radius:50% 50% 46% 46%;background:radial-gradient(ellipse at 50% 55%,#a3a5a6 0%,#6c6f70 45%,#3b3f35 85%,#2e302a 100%)}
.point{position:absolute;font-size:11.5px;line-height:1.7;color:#555;z-index:1}
.point h4{font-size:12.5px;font-weight:500;color:var(--ink);margin-bottom:6px}
.point.right{text-align:right}

/* cta */
.cta{top:2792px;height:370px;overflow:visible}
.cta .bg{position:absolute;left:0;top:22px;width:1200px;height:307px;background:var(--red)}
.cta .frame{position:absolute;left:20px;top:40px;width:1160px;height:262px;border:2px solid rgba(255,255,255,.9)}
.cta .product{position:absolute;left:690px;top:0;width:510px;height:370px;background:radial-gradient(ellipse 190px 150px at 230px 180px,#dadada 0%,#8a8a8a 45%,#2a2a2a 80%,rgba(20,20,20,0) 100%)}
.cta .eyebrow{left:98px;top:83px;color:var(--white);font-size:11px}
.cta .eyebrow::before{display:none}
.cta h2{position:absolute;left:98px;top:113px;font-size:25px;color:var(--white);white-space:nowrap}
.cta h3{position:absolute;left:98px;top:155px;font-family:var(--display);font-weight:400;font-size:15.5px;color:var(--white);text-transform:uppercase;white-space:nowrap}
.cta .btn{left:94px;top:200px;width:246px;height:42px;background:var(--red);color:var(--white);border:2px solid var(--charcoal)}

/* reviews */
.reviews{top:3162px;height:545px;background:var(--white)}
.reviews h2{position:absolute;left:0;width:1200px;text-align:center;top:92px;font-size:25px}
.reviews .intro{position:absolute;left:220px;width:760px;top:146px;text-align:center;font-size:11.8px;line-height:1.7;color:#555}
.review{position:absolute;top:232px;width:260px}
.review .head{display:flex;align-items:center;gap:12px}
.review .avatar{width:40px;height:40px;border-radius:50%;background:linear-gradient(135deg,#c9c9c9,#8d8d8d)}
.review .name{font-size:13px;font-weight:500;color:var(--ink)}
.review .meta{font-size:9px;color:#666}
.review .meta b{color:var(--gold);font-weight:400;letter-spacing:1px;margin-right:6px}
.review p{margin-top:30px;font-size:12.5px;line-height:1.72;color:#444}
.arrow-btn{position:absolute;top:329px;width:36px;height:36px;border-radius:50%;display:flex;align-items:center;justify-content:center}

/* contact */
.map{top:3707px;height:333px;background:linear-gradient(120deg,#c9c9c9 0%,#bdbdbd 40%,#d4d4d4 100%)}
.dark-base{top:4040px;height:726px;background:var(--night)}
.form-back{position:absolute;left:185px;top:3823px;width:790px;height:440px;background:var(--red)}
.form-line-r{position:absolute;left:975px;top:3860px;width:2px;height:420px;background:var(--red)}
.form-card{position:absolute;left:200px;top:3837px;width:800px;height:453px;background:var(--white);box-shadow:0 0 0 1px #eee}
.form-card h2{position:absolute;left:0;width:800px;text-align:center;top:47px;font-size:25px}
.field{position:absolute;border:1px solid #bdbdbd;font-size:9.5px;color:#8a8a8a;padding:13px 12px}
.form-card .btn{left:275px;top:353px;width:248px;height:42px;background:#676767;color:var(--white);box-shadow:inset 0 0 0 3px #676767,inset 0 0 0 4px rgba(255,255,255,.7)}

/* footer */
.site-footer{top:4290px;height:476px}
.site-footer .brand{left:198px;top:210px;color:#8d8d8d;font-size:17px}
.site-footer .brand i{background:#555}
.fcol{position:absolute;font-size:10px;color:#d6d6d6}
.fcol h5{font-size:13px;font-weight:500;color:var(--white);padding-bottom:10px;border-bottom:1px solid #555;width:122px;margin-bottom:12px}
.fcol li{list-style:none;line-height:18.5px}
.fcol .row{display:flex;align-items:center;gap:8px;line-height:26px}
.copyright{position:absolute;left:0;width:1200px;top:445px;text-align:center;font-size:10px;color:#bdbdbd}
</style>
</head>
<body>

<div class="band topbar">
  <div class="abs hours"><span>Monday — Friday: 9:00 am to 5:30 pm</span><span>Saturday: 9:00 am to 2:00 pm</span><span>Sunday: Closed</span></div>
  <div class="abs mail">
    <svg width="11" height="8" viewBox="0 0 11 8"><rect x=".5" y=".5" width="10" height="7" fill="none" stroke="#fff"/><path d="M.5 .5 5.5 4.5 10.5 .5" fill="none" stroke="#fff"/></svg>
    info@briskcoupler.com
  </div>
  <div class="social-dots"><i></i><i></i><i></i></div>
</div>

<header class="site-header">
  <div class="brand"><i></i>Brisk Coupler</div>
  <nav class="nav"><span>Home</span><span>Literature</span><span>About Us</span><span>Manufacturing</span><span>Locations</span><span>Services</span></nav>
  <div class="callout"><small>Call or Text Us :</small><strong>(123)-456-7890</strong></div>
  <div class="phone-disc"><svg width="14" height="14" viewBox="0 0 24 24"><path d="M6.6 10.8a15 15 0 0 0 6.6 6.6l2.2-2.2c.3-.3.7-.4 1-.2 1.1.4 2.3.6 3.6.6.6 0 1 .4 1 1V20c0 .6-.4 1-1 1C10.6 21 3 13.4 3 4c0-.6.4-1 1-1h3.5c.6 0 1 .4 1 1 0 1.3.2 2.5.6 3.6.1.3 0 .7-.2 1z" fill="#fff"/></svg></div>
</header>

<section class="hero">
  <div class="hero-photo" role="img" aria-label="Close-up photo of a chrome trailer hitch ball mounted on a truck receiver"></div>
  <div class="hero-shade"></div>
  <div class="stripe" style="left:40px;top:30px;width:120px;height:32px"></div>
  <div class="stripe" style="left:-40px;top:65px;width:150px;height:40px"></div>
  <div class="stripe" style="left:-60px;top:120px;width:90px;height:22px;background:#8a1606"></div>
  <h1 class="display"><span>California’s</span><span class="indent">Leading</span><span>Trailer Hitch</span></h1>
  <p>At Brisk Coupler, we specialize in the sale and installation of top-quality trailer hitches, bedliners, and pickup truck accessories for all types of trucks.</p>
  <div class="btn btn-red" style="left:92px;top:410px;width:248px;height:44px">Get a Personalized Quote Today!</div>
  <div class="btn btn-ghost" style="left:352px;top:410px;width:140px;height:44px">(123)-456-7890</div>
</section>

<div class="band features">
  <div class="shard" style="left:300px"></div>
  <div class="shard" style="left:580px"></div>
  <div class="shard" style="left:880px"></div>
  <div class="feature" style="left:95px"><i></i>Trusted Installers</div>
  <div class="feature" style="left:354px"><i></i>Quality Products</div>
  <div class="feature" style="left:650px"><i></i>Wide Selection</div>
  <div class="feature" style="left:958px"><i></i>Custom Solutions</div>
</div>

<section class="about">
  <div class="eyebrow" style="left:98px;top:56px;color:var(--ink)">About Brisk Coupler</div>
  <div class="frame"></div>
  <div class="photo" role="img" aria-label="Photo of a hand attaching a towing shackle to a truck hitch receiver"></div>
  <div class="photo-corner"></div>
  <h2 class="display">Trailer Hitch &amp; Truck Accessories Installer</h2>
  <h3>WHO WE ARE</h3>
  <p class="lead">At Brisk Coupler, we are passionate about helping truck owners enhance the performance and versatility of their vehicles. With years of experience in the industry, we have built a reputation for providing high-quality trailer hitches, bedliners, and pickup truck accessories, all backed by our exceptional customer service. We understand the importance of reliable, durable equipment when it comes to towing and protecting your truck.</p>
  <div class="vertical"><span>WHAT WE DO</span></div>
  <p class="side">That’s why we partner with industry-leading brands to offer only the best products. Our skilled technicians ensure every installation is done with precision and care, so you can hit the road with confidence.</p>
  <div class="btn btn-red" style="left:618px;top:462px;width:127px;height:44px">Read More</div>
</section>

<section class="services">
  <div class="eyebrow">Our Services</div>
  <h2 class="display">Products &amp; Services</h2>
  <p>Whether you need a heavy-duty trailer hitch for towing, a bedliner to protect your truck, or custom accessories to upgrade your ride, we have you covered.</p>
  <div class="btn btn-ghost" style="left:776px;top:77px;width:246px;height:42px;border-width:1.5px">Get a Personalized Quote Today!</div>
</section>

<div class="band cards">
  <div class="card">
    <div class="media" role="img" aria-label="Photo of a trailer coupler and safety chains on grass" style="background:linear-gradient(160deg,#9aa39a 0%,#6d7a5c 50%,#3e4a33 100%)"></div>
    <div class="label">Trailer Hitches</div>
  </div>
  <div class="card card-feature">
    <h3>Truck<br>Bedliners</h3>
    <p>Seamless, long-lasting protection applied directly to your truck bed, preventing rust and damage. Durable, easy-to-install bedliners that provide heavy-duty protection against impacts and abrasions. Tailored to fit any truck model, providing full coverage and optimal protection.</p>
    <div class="btn">Read More</div>
  </div>
  <div class="card">
    <div class="media" role="img" aria-label="Photo of truck parts including spark plugs, a filter and a fuel pump" style="background:linear-gradient(150deg,#cfcfcf 0%,#9c9c9c 55%,#6a6a6a 100%)"></div>
    <div class="label">Truck Accessories</div>
  </div>
  <div class="card">
    <div class="media" role="img" aria-label="Photo of a technician in work clothes servicing a truck" style="background:linear-gradient(160deg,#8f9aa6 0%,#4f6a8a 50%,#2d3a4b 100%)"></div>
    <div class="label">Expert Installation</div>
  </div>
</div>

<section class="why">
  <div class="watermark"><span style="left:0;top:600px">Brisk</span><span style="left:95px;top:430px">Coupler</span></div>
  <h2 class="display">Why We’re Different</h2>
  <div class="emblem" role="img" aria-label="Photo of a truck hitch framed in a large emblem shape"></div>

  <div class="point right" style="left:109px;top:218px;width:220px"><h4>Industry Expertise</h4>With years of experience in the truck accessories and towing industry, our team has deep knowledge of the products and services.</div>
  <div class="point" style="left:845px;top:185px;width:215px"><h4>Professional Installation</h4>Our certified technicians are experts in their field, ensuring that every installation is performed with precision and care.</div>
  <div class="point right" style="left:179px;top:559px;width:250px"><h4>Personalized Solutions</h4>At Brisk Coupler, we take the time to understand your specific requirements, whether it’s for towing heavy loads, protecting your truck’s.</div>
  <div class="point" style="left:750px;top:514px;width:220px"><h4>Quality Products</h4>We only partner with trusted, leading brands known for their durability and performance.</div>

  <svg class="abs" style="left:0;top:0" width="1200" height="769" viewBox="0 0 1200 769" fill="none" stroke="#222" stroke-width="1.6" stroke-linecap="round">
    <path d="M332 350 C 335 375 365 390 405 380"/><path d="M398 376 405 380 400 387"/>
    <path d="M450 460 C 425 462 410 480 410 505"/><path d="M405 498 410 505 415 498"/>
    <path d="M680 505 C 705 505 720 490 722 470"/><path d="M716 476 722 470 728 477"/>
    <path d="M790 380 C 830 380 860 365 865 335"/><path d="M859 341 865 335 870 342"/>
  </svg>
</section>

<section class="cta">
  <div class="bg"></div>
  <div class="frame"></div>
  <div class="product" role="img" aria-label="Photo of a chrome hitch ball mounted on a black ball mount"></div>
  <div class="eyebrow">Contact Us</div>
  <h2 class="display">Browse Our Selection</h2>
  <h3>Of High-Quality Truck Accessories</h3>
  <div class="btn">Get a Personalized Quote Today!</div>
</section>

<section class="reviews">
  <h2 class="display">Customer Reviews</h2>
  <p class="intro">With years of experience in the truck accessories and towing industry, at Brisk Coupler we take pride in providing top-notch service and high-quality products to truck owners across California. Don’t just take our word for it—see what our satisfied customers have to say!</p>

  <div class="review" style="left:176px">
    <div class="head"><div class="avatar" role="img" aria-label="Customer portrait"></div><div><div class="name">Nora K.</div><div class="meta"><b>★★★★★</b>1 month ago</div></div></div>
    <p>I had my trailer hitch installed by the team at Brisk Coupler, and I couldn’t be happier! The installation was quick, and the staff was incredibly knowledgeable. I’ll definitely be coming back for more truck accessories</p>
  </div>
  <div class="review" style="left:484px">
    <div class="head"><div class="avatar" role="img" aria-label="Customer portrait"></div><div><div class="name">Lena &amp; Mark P.</div><div class="meta"><b>★★★★★</b>1 month ago</div></div></div>
    <p>I had my trailer hitch installed by the team at Brisk Coupler, and I couldn’t be happier! The installation was quick, and the staff was incredibly knowledgeable. I’ll definitely be coming back for more truck accessories</p>
  </div>
  <div class="review" style="left:791px">
    <div class="head"><div class="avatar" role="img" aria-label="Customer portrait"></div><div><div class="name">Olivia S.</div><div class="meta"><b>★★★★★</b>1 month ago</div></div></div>
    <p>I had my trailer hitch installed by the team at Brisk Coupler, and I couldn’t be happier! The installation was quick, and the staff was incredibly knowledgeable. I’ll definitely be coming back for more truck accessories</p>
  </div>

  <div class="arrow-btn" style="left:95px;background:#5a5a5a"><svg width="14" height="10" viewBox="0 0 14 10" fill="none" stroke="#fff" stroke-width="1.6"><path d="M13 5H1M5 1 1 5l4 4"/></svg></div>
  <div class="arrow-btn" style="left:1070px;background:var(--red)"><svg width="14" height="10" viewBox="0 0 14 10" fill="none" stroke="#fff" stroke-width="1.6"><path d="M1 5h12M9 1l4 4-4 4"/></svg></div>
</section>

<div class="band map" role="img" aria-label="Map of California and neighbouring states showing the service area"></div>
<div class="band dark-base"></div>

<div class="form-back"></div>
<div class="form-line-r"></div>
<div class="form-card">
  <h2 class="display">How We Can Help You!</h2>
  <div class="field" style="left:98px;top:113px;width:296px;height:38px">First Name*</div>
  <div class="field" style="left:406px;top:113px;width:296px;height:38px">Last Name*</div>
  <div class="field" style="left:98px;top:168px;width:296px;height:38px">Phone Number*</div>
  <div class="field" style="left:406px;top:168px;width:296px;height:38px">Email Address*</div>
  <div class="field" style="left:98px;top:222px;width:604px;height:98px">Message*</div>
  <div class="btn">Get a Personalized Quote Today!</div>
</div>

<footer class="site-footer">
  <div class="stripe" style="left:10px;top:110px;width:100px;height:26px"></div>
  <div class="stripe" style="left:-40px;top:145px;width:120px;height:34px"></div>
  <div class="stripe" style="left:-30px;top:265px;width:80px;height:22px;background:#8a1606"></div>
  <div class="brand"><i></i>Brisk Coupler</div>

  <div class="fcol" style="left:462px;top:111px"><h5>QUICK LINKS</h5><ul><li>Home</li><li>About</li><li>Services</li><li>Products</li></ul></div>
  <div class="fcol" style="left:654px;top:111px"><h5>INSIGHTS</h5><ul><li>Research</li><li>Blog</li><li>Living Labs</li></ul></div>
  <div class="fcol" style="left:865px;top:111px"><h5>CONTACT US</h5>
    <div class="row"><svg width="10" height="10" viewBox="0 0 24 24"><path d="M6.6 10.8a15 15 0 0 0 6.6 6.6l2.2-2.2c.3-.3.7-.4 1-.2 1.1.4 2.3.6 3.6.6.6 0 1 .4 1 1V20c0 .6-.4 1-1 1C10.6 21 3 13.4 3 4c0-.6.4-1 1-1h3.5c.6 0 1 .4 1 1 0 1.3.2 2.5.6 3.6.1.3 0 .7-.2 1z" fill="#e8270f"/></svg>+ (123)-456-789</div>
    <div class="row"><svg width="10" height="8" viewBox="0 0 11 8"><rect x=".5" y=".5" width="10" height="7" fill="#e8270f"/><path d="M.5 .5 5.5 4.5 10.5 .5" fill="none" stroke="#fff"/></svg>info@briskcoupler.com</div>
  </div>

  <div class="fcol" style="left:462px;top:245px"><h5>SERVICES</h5><ul><li>Alignment</li><li>Aluminum Tank Repair</li><li>Auto &amp; Truck Lift and Lower</li><li>Brake Relining</li><li>CNG &amp; LNG</li><li>and more..</li></ul></div>
  <div class="fcol" style="left:654px;top:245px"><h5>ABOUT US</h5><ul><li>Research</li><li>Blog</li><li>Living Labs</li></ul></div>
  <div class="fcol" style="left:865px;top:245px"><h5>SOCIAL</h5><div class="social-dots" style="gap:8px;margin-top:4px"><i style="width:20px;height:20px;background:#d6d6d6"></i><i style="width:20px;height:20px;background:#d6d6d6"></i><i style="width:20px;height:20px;background:#d6d6d6"></i></div></div>

  <div class="copyright">© Copyright 2024 - brisk coupler. All Rights Reserved.</div>
</footer>

</body>
</html>
```